KVT Roofing Pty Ltd

We are a high end residential Roofing company
We would like something silimar to the attached logo with the same color scheme

Target Market(s)

High end residential Builders & Architects

Industry/Entity Type

Residential

```html
<!DOCTYPE html>
<html lang="en">
<head>
<meta charset="utf-8">
<title>KVT Roofing – Business Card</title>
<link rel="stylesheet" href="https://fonts.googleapis.com/css2?family=Roboto+Condensed:wght@400&display=swap">
<style>
  :root {
    --page-bg: #e9e9e9;
    --card-white: #ffffff;
    --card-grey-light: #ececec;
    --slate: #45525d;
    --slate-dark: #3a4650;
    --accent-blue: #1296d3;
    --ink: #4a5661;
    --text-light: #ffffff;
  }
  * { margin: 0; padding: 0; box-sizing: border-box; }
  html, body {
    width: 1200px;
    height: 1200px;
    overflow: hidden;
    background: var(--page-bg);
    font-family: "Roboto Condensed", "Arial Narrow", sans-serif;
  }
  .canvas {
    position: relative;
    width: 1200px;
    height: 1200px;
    display: flex;
    align-items: center;
    justify-content: center;
  }
  .business-card {
    position: relative;
    width: 1000px;
    height: 610px;
    background: radial-gradient(ellipse at 70% 10%, var(--card-white) 0%, var(--card-grey-light) 100%);
    box-shadow: 0 10px 30px rgba(0,0,0,0.18);
    overflow: hidden;
  }
  .card-band {
    position: absolute;
    inset: 0;
    width: 100%;
    height: 100%;
  }
  .brand {
    position: absolute;
    left: 70px;
    top: 175px;
    display: flex;
    align-items: center;
    gap: 18px;
  }
  .brand-square {
    width: 46px;
    height: 46px;
    background: var(--slate);
  }
  .brand-name {
    font-size: 40px;
    color: var(--slate);
    letter-spacing: 1px;
    text-transform: uppercase;
  }
  .identity {
    position: absolute;
    right: 70px;
    top: 62px;
    text-align: right;
  }
  .person-name {
    font-size: 50px;
    color: var(--ink);
    line-height: 1.1;
  }
  .person-title {
    font-size: 40px;
    color: var(--accent-blue);
    line-height: 1.2;
    margin-top: 6px;
  }
  .contact-list {
    position: absolute;
    left: 70px;
    top: 385px;
    list-style: none;
  }
  .contact-item {
    display: flex;
    align-items: center;
    gap: 22px;
    height: 68px;
    font-size: 36px;
    color: var(--text-light);
  }
  .contact-icon {
    width: 40px;
    height: 40px;
    flex: none;
    fill: var(--accent-blue);
  }
</style>
</head>
<body>
<main class="canvas">
  <article class="business-card">
    <svg class="card-band" viewBox="0 0 1000 610" preserveAspectRatio="none" aria-hidden="true">
      <defs>
        <linearGradient id="slate-fill" x1="0" y1="0" x2="1" y2="1">
          <stop offset="0" stop-color="var(--slate)"/>
          <stop offset="1" stop-color="var(--slate-dark)"/>
        </linearGradient>
      </defs>
      <polygon points="0,336 1000,208 1000,222 0,350" fill="var(--accent-blue)"/>
      <polygon points="0,350 1000,222 1000,610 0,610" fill="url(#slate-fill)"/>
    </svg>

    <div class="brand">
      <span class="brand-square"></span>
      <span class="brand-name">KVT Roofing</span>
    </div>

    <header class="identity">
      <h1 class="person-name">Marcus Ellery</h1>
      <p class="person-title">General Manager</p>
    </header>

    <ul class="contact-list">
      <li class="contact-item">
        <svg class="contact-icon" viewBox="0 0 24 24" aria-hidden="true">
          <path d="M12 2a7 7 0 0 0-7 7c0 5.2 7 13 7 13s7-7.8 7-13a7 7 0 0 0-7-7zm0 9.6A2.6 2.6 0 1 1 12 6.4a2.6 2.6 0 0 1 0 5.2z"/>
        </svg>
        <span>218 Harlow Street, Port Ardell</span>
      </li>
      <li class="contact-item">
        <svg class="contact-icon" viewBox="0 0 24 24" aria-hidden="true">
          <path d="M6.6 10.8a15.1 15.1 0 0 0 6.6 6.6l2.2-2.2a1 1 0 0 1 1-.25 11.4 11.4 0 0 0 3.6.57 1 1 0 0 1 1 1V20a1 1 0 0 1-1 1A17 17 0 0 1 3 4a1 1 0 0 1 1-1h3.5a1 1 0 0 1 1 1c0 1.25.2 2.45.57 3.57a1 1 0 0 1-.25 1z"/>
        </svg>
        <span>0400 555 218</span>
      </li>
      <li class="contact-item">
        <svg class="contact-icon" viewBox="0 0 24 24" aria-hidden="true">
          <path d="M2 5h20v2.2l-10 6.3L2 7.2z"/>
          <path d="M2 9.4l10 6.3 10-6.3V19H2z"/>
        </svg>
        <span>mellery@kvtsteelroofing.com.au</span>
      </li>
    </ul>
  </article>
</main>
</body>
</html>
```